Bows Catalog Cover

Cover Page for a catalog for bows. Same logo MOR Morvane Alpina Cordaria.
Catalog overview: https://www.folioworks-demo.net/MOR-Morvane-Alpina-Cordaria/catalogs/MOR-catalog.html
No instruments, no scores, Only bows or bow parts (head, frog ...). Drawings or pictures.

Target Market(s)

Violin makers and reseller

Requirements
Must have
• bows or bow parts
Nice to have
• Drawings and or pictures
Should not have
• full Instruments or scores

```html
<!DOCTYPE html>
<html lang="fr">
<head>
<meta charset="utf-8">
<title>Archets 2021 – MOR Morvane Alpina Cordaria</title>
<link rel="stylesheet" href="https://fonts.googleapis.com/css2?family=Roboto+Condensed:wght@400;700&display=swap">
<style>
  :root {
    --backdrop: #ebebeb;
    --cover: #f6f7f8;
    --ink: #1c1213;
    --brand: #4a2fa8;
    --bow-wood: #3a211d;
    --bow-hair: #e9d7a6;
  }
  * { margin: 0; padding: 0; box-sizing: border-box; }
  html, body {
    width: 1200px;
    height: 840px;
    overflow: hidden;
    background: var(--backdrop);
  }
  .canvas {
    position: relative;
    width: 1200px;
    height: 840px;
    display: flex;
    align-items: center;
    justify-content: center;
  }
  .cover {
    position: relative;
    width: 560px;
    height: 792px;
    background: var(--cover);
    box-shadow: 0 6px 24px rgba(0,0,0,0.12);
    overflow: hidden;
    font-family: "Roboto Condensed", "Arial Narrow", sans-serif;
    color: var(--ink);
  }
  .cover-title {
    position: absolute;
    top: 40px;
    right: 44px;
    text-align: right;
    line-height: 0.86;
  }
  .cover-title .series {
    display: block;
    font-size: 66px;
    font-weight: 700;
    letter-spacing: 1px;
  }
  .cover-title .year {
    display: block;
    font-size: 200px;
    font-weight: 700;
    letter-spacing: -6px;
    margin-right: -4px;
  }
  .bow-heads {
    position: absolute;
    left: 0;
    bottom: 0;
    width: 560px;
    height: 792px;
  }
  .brand {
    position: absolute;
    left: 28px;
    top: 592px;
    display: flex;
    align-items: center;
    gap: 8px;
    color: var(--brand);
  }
  .brand-dot {
    width: 18px;
    height: 18px;
    border-radius: 50%;
    background: var(--brand);
  }
  .brand-text .name {
    display: block;
    font-size: 28px;
    font-weight: 700;
    line-height: 1;
    letter-spacing: 1px;
  }
  .brand-text .tagline {
    display: block;
    font-size: 7px;
    font-weight: 700;
    letter-spacing: 0.6px;
    text-transform: uppercase;
    margin-top: 2px;
  }
</style>
</head>
<body>
  <main class="canvas">
    <article class="cover">
      <h1 class="cover-title">
        <span class="series">ARCHETS</span>
        <span class="year">2021</span>
      </h1>

      <svg class="bow-heads" viewBox="0 0 560 792" role="img" aria-label="Photographie d'une rangée de têtes d'archets en bois brun avec leurs mèches de crin, en diagonale">
        <defs>
          <linearGradient id="bowTone" x1="0" y1="0" x2="1" y2="0">
            <stop offset="0" stop-color="#3a211d"/>
            <stop offset="0.35" stop-color="#6b4a35"/>
            <stop offset="0.6" stop-color="#c9b184"/>
            <stop offset="1" stop-color="#3a211d"/>
          </linearGradient>
        </defs>
        <polygon points="150,640 560,330 560,792 150,792" fill="url(#bowTone)" opacity="0.85"/>
      </svg>

      <div class="brand">
        <span class="brand-dot"></span>
        <span class="brand-text">
          <span class="name">MOR</span>
          <span class="tagline">Morvane Alpina Cordaria</span>
        </span>
      </div>
    </article>
  </main>
</body>
</html>
```